Business Card Designs - Please read overview

We are an online forex trading company with offices in a few countries in Africa, Middle East and Sub Continent. www.brelvantmarkets.com . We allow people to trade online using our platform. We are also involved in Gold trading Online and Physical but Forex side is bigger.

We want people to figure out that we are a Cool/ Innovative/ trustworthy/ Personal/ Global/ Regulated Financial Services company.

That card needs to be double sided, Definitely not plain at the back.

We would want to somehow tell that we are global .. Currently we list the countries, and because half the people still use a different design - they use a map with points on the map. I am sure there could be better ways.

We deal with a few Stock exchanges and we can put their logos if you feel it adds credibility. Not necessary. Exchanges and regulatory bodies. KRT Mauritius / NWD South Africa / LQEX / TVRA just for you to see if their logos would look interesting or not.

Also, We use a slogan " The Opportunity"

Selim Varokhan
CEO

Marcus Edley
VP Strategic Partnerships

Target Market(s)

Do it yourself traders. People who have some disposable income who go online and trade themselves. Mostly Male, 65% . Ages between 23-50.

Industry/Entity Type

Trade

Requirements
Must have
• Somewhere on the card we have to say the following words -
" Brelvant Markets and Forex trading (Pty) Ltd is a Juristic Rep of FSP-47362 "

Must be double sided. Must have something at the back. Map / logo/ domain/ whatever.

Should not have
• We are not big fans of QR Codes.

```html
<!DOCTYPE html>
<html lang="en">
<head>
<meta charset="utf-8">
<title>Brelvant Markets — Business Card</title>
<link rel="stylesheet" href="https://fonts.googleapis.com/css2?family=Oswald:wght@500;700&family=Roboto+Condensed:wght@400;700&display=swap">
<style>
  :root {
    --backdrop: #b7b9b9;
    --card: #ecebe8;
    --ink: #1d1d1d;
    --ink-soft: #4a4a4a;
    --gold: #f2c21b;
    --map-grey: #838385;
    --badge-grey: #5c5c5c;
  }
  * { box-sizing: border-box; margin: 0; padding: 0; }
  html, body { width: 1200px; height: 1012px; overflow: hidden; }
  body {
    background: var(--backdrop);
    font-family: "Roboto Condensed", Arial, sans-serif;
    color: var(--ink);
    display: flex;
    flex-direction: column;
    align-items: center;
    justify-content: space-evenly;
  }
  .card {
    position: relative;
    width: 770px;
    height: 440px;
    background: var(--card);
    box-shadow: 0 6px 18px rgba(0,0,0,0.18);
  }

  /* ---------- back side ---------- */
  .brand {
    position: absolute;
    display: flex;
    align-items: center;
    gap: 10px;
    font-family: "Oswald", Arial, sans-serif;
    font-weight: 700;
    color: var(--ink);
    letter-spacing: 0.04em;
    text-transform: uppercase;
  }
  .brand-square { width: 22px; height: 22px; background: var(--gold); }
  .back .brand { left: 56px; top: 70px; font-size: 28px; }
  .contacts {
    position: absolute;
    left: 56px;
    top: 140px;
    list-style: none;
    font-size: 15px;
    line-height: 1.25;
  }
  .contacts li { margin-bottom: 12px; }
  .contacts .label {
    display: block;
    font-weight: 700;
    font-size: 12px;
    letter-spacing: 0.06em;
    text-transform: uppercase;
  }
  .contacts .value { color: var(--ink-soft); }
  .contacts .web { font-weight: 700; color: var(--ink); margin-top: 6px; }
  .presence-map {
    position: absolute;
    right: 40px;
    top: 36px;
    width: 400px;
    height: 340px;
    border-radius: 60px 120px 80px 140px;
    background: radial-gradient(ellipse at 45% 45%, #8c8c8e 0%, var(--map-grey) 70%, #9a9a9c 100%);
  }

  /* ---------- front side ---------- */
  .front .brand { left: 70px; top: 210px; font-size: 30px; }
  .legal {
    position: absolute;
    left: 70px;
    top: 262px;
    width: 260px;
    font-size: 13px;
    font-weight: 700;
    line-height: 1.3;
  }
  .person { position: absolute; left: 420px; top: 70px; }
  .person-name {
    display: inline-block;
    background: var(--gold);
    color: var(--ink);
    font-family: "Oswald", Arial, sans-serif;
    font-weight: 700;
    font-size: 26px;
    letter-spacing: 0.12em;
    padding: 2px 12px;
  }
  .person-role {
    font-family: "Oswald", Arial, sans-serif;
    font-weight: 500;
    font-size: 20px;
    margin-top: 6px;
  }
  .person-contact { list-style: none; margin-top: 8px; margin-left: 34px; font-size: 16px; line-height: 1.6; }
  .person-contact b { display: inline-block; width: 20px; font-size: 13px; }
  .slogan {
    position: absolute;
    left: 420px;
    top: 290px;
    font-family: "Oswald", Arial, sans-serif;
    font-weight: 500;
    font-size: 17px;
    letter-spacing: 0.28em;
  }
  .partners {
    position: absolute;
    left: 420px;
    top: 330px;
    display: flex;
    gap: 22px;
    align-items: center;
  }
  .partner-badge { width: 38px; height: 38px; background: var(--badge-grey); }
  .partner-badge.round { border-radius: 50%; }
  .partner-badge.wide { width: 70px; height: 26px; }
</style>
</head>
<body>

  <section class="card back" aria-label="Card back">
    <div class="brand"><span class="brand-square"></span>Brelvant</div>
    <ul class="contacts">
      <li><span class="label">Account Support</span><span class="value">support@brelvantmarkets.com</span></li>
      <li><span class="label">Technical Customer Support</span><span class="value">tech@brelvantmarkets.com</span></li>
      <li><span class="label">Sales</span><span class="value">sales@brelvantmarkets.com</span></li>
      <li><span class="label">Trading Desk</span><span class="value">trading@brelvantmarkets.com</span></li>
      <li class="web">www.brelvantmarkets.com</li>
    </ul>
    <div class="presence-map" role="img" aria-label="Grey map of Africa, the Middle East and Asia with gold pins on office countries: Nigeria, Ghana, Tanzania, South Africa, Mauritius, Pakistan, Bangladesh"></div>
  </section>

  <section class="card front" aria-label="Card front">
    <div class="brand"><span class="brand-square"></span>Brelvant</div>
    <p class="legal">Brelvant Markets and Forex trading (Pty) Ltd is a Juristic Rep of FSP-47362</p>
    <div class="person">
      <span class="person-name">Selim Varokhan</span>
      <p class="person-role">CEO</p>
      <ul class="person-contact">
        <li><b>e</b>selim@brelvantmarkets.com</li>
        <li><b>P</b>999 99 9999</li>
      </ul>
    </div>
    <p class="slogan">The Opportunity.</p>
    <div class="partners" aria-label="Exchange and regulator listings">
      <span class="partner-badge"></span>
      <span class="partner-badge wide"></span>
      <span class="partner-badge"></span>
      <span class="partner-badge round"></span>
    </div>
  </section>

</body>
</html>
```